A comprehensive online math curriculum teaching service needs a Landing Page design

We need a Landing Page design for a startup company based in Edmonton, Alberta, Canada, called Trivento Numérica. Trivento Numérica is a comprehensive online math curriculum service for independently schooled students in grades 6-12 worldwide. Instruction is delivered through a one-on-one, virtual, adaptive classroom that uses integrated, interactive digital whiteboards for both teachers and students, with a standard modular lesson workflow for mastering math. Trivento Numérica is designed to help students from all socioeconomic backgrounds master mathematics.

The landing Page should use the same colour scheme as our recently designed PowerPoint template (attached for reference: Design 36712224). Our logo is in the PowerPoint template. I also attached a draft wireframe of our landing page to guide the design.

Target Market(s)

Independently schooled students in grades 6 through 12 worldwide

Industry/Entity Type

Education - Mathematics teaching

Requirements
Must have
• Consistent colours with PowerPoint design

```html
<!DOCTYPE html>
<html lang="en">
<head>
<meta charset="utf-8">
<title>Trivento Numérica — Online Math Curriculum</title>
<link href="https://fonts.googleapis.com/css2?family=Catamaran:wght@500;600;700;800&family=Nunito+Sans:ital,wght@0,400;0,600;0,700;1,400;1,600&display=swap" rel="stylesheet">
<style>
:root{
  --navy:#1f2a38;
  --navy-deep:#18212d;
  --green:#3b7a57;
  --green-dark:#2f6a4a;
  --chalk-a:#2d6a48;
  --chalk-b:#1e4e36;
  --ink:#1b1f24;
  --muted:#444c55;
  --rule:#dcdfe3;
  --soft:#eef2ef;
  --blue:#3b82f6;
  --card:#eaf0fb;
  --icon:#3d5566;
  --white:#ffffff;
  --black:#050505;
}
*{box-sizing:border-box;margin:0;padding:0}
html,body{width:1200px;height:3949px;overflow:hidden}
body{font-family:"Nunito Sans",sans-serif;color:var(--ink);background:var(--white);position:relative}
.head{font-family:"Catamaran",sans-serif}
.btn{display:inline-flex;align-items:center;justify-content:center;font-family:"Nunito Sans",sans-serif;font-weight:700;font-size:15px;border-radius:3px;text-decoration:none;box-shadow:0 2px 4px rgba(0,0,0,.2)}
.btn-green{background:var(--green);color:var(--white)}
.btn-navy{background:var(--navy);color:var(--white)}
.btn-white{background:var(--white);color:var(--navy)}

/* header */
.site-header{position:absolute;left:0;top:0;width:1200px;height:100px;background:var(--white)}
.brand{position:absolute;left:110px;top:22px;display:flex;align-items:flex-start;gap:14px}
.brand-mark{width:32px;height:32px;background:var(--navy);border-radius:50%;margin-top:4px}
.brand-name{font-size:29px;font-weight:500;color:var(--navy);line-height:1}
.brand-tag{font-size:13px;color:var(--muted);margin-top:10px}
.header-cta{position:absolute;top:13px;right:112px;display:flex;gap:14px}
.header-cta .btn{height:37px;padding:0 15px}
.main-nav{position:absolute;top:66px;right:112px;display:flex;gap:48px;font-size:16px;font-weight:600;color:var(--ink)}

/* hero */
.hero{position:absolute;left:0;top:100px;width:1200px;height:551px;background:linear-gradient(135deg,#253243,var(--navy) 50%,var(--navy-deep))}
.hero-copy{position:absolute;left:108px;top:108px;width:462px;color:var(--white)}
.hero-copy h1{font-size:52px;font-weight:700;line-height:1.05;margin-bottom:18px}
.hero-copy p{font-size:14px;line-height:27.5px;width:455px}
.hero-copy .actions{display:flex;gap:18px;margin-top:30px}
.hero-copy .actions .btn{height:38px;padding:0 18px}
.hero-visual{position:absolute;left:643px;top:89px;width:445px;height:367px;border-radius:20px;background:linear-gradient(135deg,#f3f6f4,#ffffff 45%,#fff3e6)}

/* registration */
.register{position:absolute;left:0;top:651px;width:1200px;height:733px;text-align:center}
.register h2{font-size:33px;font-weight:700;line-height:41px;margin-top:92px}
.rule{width:58px;height:3px;background:var(--green);margin:14px auto 0}
.register .lead{font-size:15px;color:var(--muted);line-height:25px;width:860px;margin:22px auto 0}
.stats{width:937px;height:108px;margin:28px auto 0;border:1.5px solid var(--rule);display:flex;align-items:center}
.stat{flex:1;position:relative}
.stat + .stat::before{content:"";position:absolute;left:0;top:6px;height:62px;border-left:1.5px solid var(--rule)}
.stat b{display:block;font-family:"Catamaran",sans-serif;font-size:42px;font-weight:700;color:var(--green);line-height:1}
.stat span{display:block;font-size:16px;color:var(--muted);margin-top:14px}
.register .body{font-size:15px;color:var(--muted);line-height:27px;width:920px;margin:28px auto 0}
.register .body strong{color:var(--ink)}
.register .actions{display:flex;justify-content:center;gap:16px;margin-top:22px}
.register .actions .btn{height:38px;padding:0 15px}

/* proficiency */
.proficiency{position:absolute;left:0;top:1384px;width:1200px;height:773px;background:radial-gradient(ellipse at 50% 40%,var(--chalk-a),var(--chalk-b) 85%);color:var(--white)}
.proficiency h2{position:absolute;top:78px;width:100%;text-align:center;font-size:37px;font-weight:700}
.proficiency .rule{position:absolute;top:128px;left:571px;margin:0;background:var(--white)}
.proficiency .sub{position:absolute;top:146px;width:100%;text-align:center;font-size:20px;font-weight:600}
.proficiency .note{position:absolute;top:176px;width:100%;text-align:center;font-size:14px}
.wheel{position:absolute;left:400px;top:254px;width:400px;height:400px}
.challenge{position:absolute;width:290px}
.challenge h3{font-size:17px;font-weight:700;margin-bottom:8px}
.challenge p{font-size:14px;line-height:23px}
.challenge.left{text-align:right}

/* how it works */
.how{position:absolute;left:0;top:2157px;width:1200px;height:723px;text-align:center}
.how h2{font-size:33px;font-weight:700;line-height:40px;margin-top:88px}
.how .lead{font-size:17px;line-height:26px;color:var(--muted);width:820px;margin:18px auto 0}
.columns{position:absolute;left:110px;top:236px;width:978px;display:flex;gap:46px;text-align:left}
.column{flex:1}
.column-head{height:50px;display:flex;align-items:center;padding-left:74px;color:var(--white);font-family:"Catamaran",sans-serif;font-size:21px;font-weight:700}
.column.method .column-head{background:var(--green)}
.column.classroom .column-head{background:var(--navy)}
.feature{display:flex;gap:16px;padding:18px 20px;background:linear-gradient(90deg,var(--card),#f7f9fd 80%,#fff);margin-top:8px}
.column .feature:first-of-type{margin-top:0}
.feature .icon{flex:0 0 36px;height:36px;border-radius:50%;border:1.5px solid var(--blue);display:flex;align-items:center;justify-content:center}
.feature h4{font-size:15px;font-weight:600;margin-bottom:10px}
.feature p{font-size:12.5px;line-height:20px;color:var(--muted)}
.feature p + p{margin-top:20px}

/* lesson design */
.lesson{position:absolute;left:0;top:2880px;width:1200px;height:698px;background:var(--soft);text-align:center}
.lesson h2{font-size:33px;font-weight:700;margin-top:62px}
.tabs{position:absolute;top:150px;left:129px;display:flex;gap:36px}
.tab{height:48px;display:flex;align-items:center;padding:0 16px;border-radius:3px;color:var(--white);font-weight:700;font-size:16px;text-align:left}
.tab.grades-low{background:var(--green);height:46px}
.tab.grades-high{background:var(--blue);width:402px;height:72px;padding:0 42px;line-height:26px}
.timeline{position:absolute;top:262px;left:110px;width:1000px;height:240px}
.timeline .line{position:absolute;left:122px;right:122px;top:79px;border-top:1.5px solid #d2d8d4}
.step{position:absolute;width:240px;text-align:center}
.step .time{font-size:15px;color:var(--muted)}
.step .num{width:58px;height:58px;border-radius:50%;background:var(--blue);color:var(--white);font-family:"Catamaran",sans-serif;font-size:26px;font-weight:700;display:flex;align-items:center;justify-content:center;margin:19px auto 0;box-shadow:0 0 0 5px #fff}
.step h3{font-size:15px;font-weight:700;margin-top:14px;letter-spacing:.2px}
.step p{font-size:14.5px;line-height:21px;color:var(--muted);margin-top:8px}
.lesson .total{position:absolute;top:519px;width:100%;font-size:17px;font-style:italic;font-weight:600;color:var(--blue)}
.lesson .btn{position:absolute;top:553px;left:518px;height:38px;padding:0 18px}

/* footer */
.site-footer{position:absolute;left:0;top:3578px;width:1200px;height:371px;background:var(--black);color:var(--white);text-align:center}
.footer-brand{display:flex;justify-content:center;align-items:flex-start;gap:18px;margin-top:94px}
.footer-brand .brand-mark{background:var(--white);width:40px;height:40px;margin-top:0}
.footer-brand .brand-name{color:var(--white);font-size:37px}
.footer-brand .brand-tag{color:#ddd;font-size:16px;margin-top:14px;text-align:left}
.footer-nav{display:flex;justify-content:center;gap:46px;margin-top:36px;font-size:16px;font-weight:600}
.copyright{margin-top:38px;font-size:15px;font-weight:600}
</style>
</head>
<body>

<header class="site-header">
  <div class="brand">
    <div class="brand-mark"></div>
    <div>
      <div class="brand-name">Trivento Numérica</div>
      <div class="brand-tag">Inspiring Math · Empowering Learning</div>
    </div>
  </div>
  <div class="header-cta">
    <a class="btn btn-green">Register a Student</a>
    <a class="btn btn-navy">Free Consultation</a>
  </div>
  <nav class="main-nav"><span>Features</span><span>Program</span><span>Tuition</span><span>About Us</span><span>Contact Us</span></nav>
</header>

<section class="hero">
  <div class="hero-copy">
    <h1 class="head">Trivento Numérica</h1>
    <p>Accelerated educational outcome is a comprehensive online math curriculum teaching service for independently schooled students in <strong>grades 6 through 12 worldwide</strong>. Teaching is done through our math academy, a one-on-one, virtual adaptive classroom that uses integrated, interactive digital whiteboards for both teachers and students.&nbsp; Trivento Numérica Academy will open its virtual doors for the first cohort of <strong>grade 6 students in September 2026.</strong></p>
    <div class="actions">
      <a class="btn btn-white">Free Consultation</a>
      <a class="btn btn-green">Register a Student</a>
    </div>
  </div>
  <div class="hero-visual" role="img" aria-label="Illustration of a teacher at a chalkboard connected to three students studying at desks"></div>
</section>

<section class="register">
  <h2 class="head">Registration for Term One math classes opens<br>on June 1, 2026 and closes in the middle of August 2026.</h2>
  <div class="rule"></div>
  <p class="lead">Trivento Numérica is designed to help students from all socioeconomic backgrounds master mathematics. We teach comprehensive grade 6-12 math curricula to independently schooled students.</p>
  <div class="stats">
    <div class="stat" style="flex:0 0 170px"><b>90+</b><span>Lessons</span></div>
    <div class="stat" style="flex:0 0 412px"><b>20+</b><span>Homework questions and answers per lesson</span></div>
    <div class="stat"><b>20+</b><span>Assessment tests per grade program.</span></div>
  </div>
  <p class="body">Online, interactive math sessions are delivered in secure virtual classrooms with integrated digital whiteboards for both teacher and student. Real-time one-on-one synchronous math sessions led by qualified experts.</p>
  <p class="body" style="margin-top:26px">We teach modular math lessons that use an incremental development methodology, grounded in continuous practice and review.<br>Our math lessons are designed in small <strong>1 ½-hour units,</strong> each covering a new math concept that can be taught in<br><strong>20 minutes,</strong> allowing students ample time to practice the newly introduced math skills daily.</p>
  <div class="actions">
    <a class="btn btn-green">Register a Student</a>
    <a class="btn btn-navy">Free Consultation</a>
  </div>
</section>

<section class="proficiency">
  <h2 class="head">Proficiency</h2>
  <div class="rule"></div>
  <p class="sub">Making math education engaging, effective, and within everyone’s reach.</p>
  <p class="note">Teaching math to independently schooled students is not easy. We know the challenges:</p>

  <svg class="wheel" viewBox="0 0 400 400" aria-hidden="true">
    <g fill="#ffffff">
      <path id="seg" d="M284.6,156.9 L364.8,116 A185 185 0 0 1 364.8,284 L284.6,243.1 A95 95 0 0 0 284.6,156.9 Z"/>
      <use href="#seg" transform="rotate(60 200 200)"/>
      <use href="#seg" transform="rotate(120 200 200)"/>
      <use href="#seg" transform="rotate(180 200 200)"/>
      <use href="#seg" transform="rotate(240 200 200)"/>
      <use href="#seg" transform="rotate(300 200 200)"/>
    </g>
    <g fill="none" stroke="var(--icon)" stroke-width="1.6" stroke-linecap="round" stroke-linejoin="round">
      <!-- expertise: person with stars (top-left) -->
      <g transform="translate(114 63)">
        <circle cx="16" cy="16" r="6"/>
        <path d="M6 32c1-8 19-8 20 0"/>
        <path d="M4 6l1.5 3 3 .4-2.2 2 .6 3-2.9-1.5-2.9 1.5.6-3L.5 9.4l3-.4z"/>
        <path d="M16 0l1.5 3 3 .4-2.2 2 .6 3-2.9-1.5-2.9 1.5.6-3-2.2-2 3-.4z"/>
        <path d="M28 6l1.5 3 3 .4-2.2 2 .6 3-2.9-1.5-2.9 1.5.6-3-2.2-2 3-.4z"/>
      </g>
      <!-- curriculum: document (top-right) -->
      <g transform="translate(254 63)">
        <rect x="4" y="2" width="20" height="26" rx="1.5"/>
        <path d="M8 9h12M8 14h12M8 19h8"/>
        <path d="M18 26l7-4 7 4-7 4z"/>
      </g>
      <!-- advanced math: chart (right) -->
      <g transform="translate(324 184)">
        <path d="M2 2v28h30"/>
        <path d="M6 24l7-9 6 5 10-13"/>
        <path d="M25 7h4v4"/>
      </g>
      <!-- fun: grid sheet (bottom-right) -->
      <g transform="translate(254 305)">
        <rect x="2" y="4" width="28" height="24" rx="1.5"/>
        <path d="M2 12h28M2 20h28M11 4v24M20 4v24"/>
      </g>
      <!-- assessment: gauge (bottom-left) -->
      <g transform="translate(114 305)">
        <path d="M3 26a13 13 0 0 1 26 0"/>
        <path d="M16 26l6-9"/>
        <circle cx="16" cy="26" r="2"/>
        <path d="M7 20l2 1M25 20l-2 1M16 13v2"/>
      </g>
      <!-- understanding: chat (left) -->
      <g transform="translate(44 184)">
        <rect x="2" y="4" width="20" height="14" rx="2"/>
        <path d="M7 18l-3 5 7-5"/>
        <path d="M12 22h16a2 2 0 0 0 2-2V12"/>
        <path d="M6 9h12M6 13h8"/>
      </g>
    </g>
    <circle cx="200" cy="200" r="82" fill="#ffffff"/>
    <circle cx="200" cy="200" r="70" fill="#e9eef6" role="img" aria-label="Illustration of a teacher surrounded by math symbols"/>
  </svg>

  <div class="challenge left" style="left:170px;top:244px;width:300px"><h3>Limited subject expertise</h3><p>Struggling with advanced topics, forgotten knowledge, and specialized methods.</p></div>
  <div class="challenge" style="left:765px;top:232px"><h3>Curriculum challenges</h3><p>How can I choose the right curriculum and supplementary materials? Can I successfully adapt pre-made plans?</p></div>
  <div class="challenge left" style="left:98px;top:423px;width:300px"><h3>Ensuring conceptual understanding</h3><p>Over-reliance on procedures. Bridging the<br>“why” of math and real-world applications.</p></div>
  <div class="challenge" style="left:811px;top:420px"><h3>Preparing for advanced math</h3><p>Am I preparing my child for advanced math and for successfully transitioning into higher education, skilled jobs, or entrepreneurship?</p></div>
  <div class="challenge left" style="left:128px;top:592px;width:330px"><h3>Assessment and feedback</h3><p>Am I using the proper evaluation process to assess<br>my child’s progress and identify their weaknesses?</p></div>
  <div class="challenge" style="left:760px;top:592px;width:330px"><h3>Keeping math fun and engaging</h3><p>Creativity struggles, gamification challenges and overcoming math fatigue.</p></div>
</section>

<section class="how">
  <h2 class="head">How Trivento Numérica Works</h2>
  <div class="rule"></div>
  <p class="lead">Teaching comprehensive math curricula to independently schooled students in grades 6-12 through secure virtual classrooms.</p>
  <div class="columns">
    <div class="column method">
      <div class="column-head">Pedagogical Methodology</div>
      <div class="feature"><div class="icon"><svg width="18" height="18" viewBox="0 0 18 18" fill="none" stroke="#3b82f6" stroke-width="1.5"><rect x="3" y="2" width="12" height="14" rx="1"/><path d="M6 6h6M6 9h6M6 12h4"/></svg></div>
        <div><h4>Effective Curriculum</h4><p>Time-tested and proven pedagogical methodology with three pillars: (1) new math concepts built on previously taught ones; (2) daily review of earlier math concepts to increase understanding; and (3) frequent, cumulative assessments to ensure students master each math skill as new ones are added.</p></div></div>
      <div class="feature"><div class="icon"><svg width="18" height="18" viewBox="0 0 18 18" fill="none" stroke="#3b82f6" stroke-width="1.5"><circle cx="9" cy="7" r="4"/><path d="M7 12h4M7 15h4"/></svg></div>
        <div><h4>Innovative Lesson Design</h4><p>Standard, modular 1 ½ hour lesson workflows designed to accelerate students’ mastery of math skills and concepts.</p></div></div>
    </div>
    <div class="column classroom">
      <div class="column-head">Virtual Classroom</div>
      <div class="feature"><div class="icon"><svg width="18" height="18" viewBox="0 0 18 18" fill="none" stroke="#3b82f6" stroke-width="1.5"><rect x="2" y="3" width="14" height="9" rx="1"/><path d="M9 12v4M6 16h6"/></svg></div>
        <div><h4>Personalized Whiteboards</h4><p>Every student gets an individual digital whiteboard, where they can draw, write text and equations, work on practice problems, homework, and tests.</p><p>The students only see the teacher and their whiteboard.</p></div></div>
      <div class="feature"><div class="icon"><svg width="18" height="18" viewBox="0 0 18 18" fill="none" stroke="#3b82f6" stroke-width="1.5"><circle cx="9" cy="6" r="3"/><path d="M3 16c1-4 11-4 12 0"/></svg></div>
        <div><h4>Interactive Sessions</h4><p>Engage with dynamic content, real-time problem solving and feedback, and interactive tools that make math concepts come alive.</p></div></div>
    </div>
  </div>
</section>

<section class="lesson">
  <h2 class="head">Innovative Lesson Design</h2>
  <div class="rule"></div>
  <div class="tabs">
    <div class="tab grades-low">1 and 2 Hour Session Lesson Workflow Grades 6 to 8</div>
    <div class="tab grades-high">1 and 2 Hour Session Lesson Workflow<br>Grades 9 to 12</div>
  </div>
  <div class="timeline">
    <div class="line"></div>
    <div class="step" style="left:3px"><div class="time">25 minutes</div><div class="num">1</div><h3>NEW CONCEPTS</h3><p>Introduces new math concepts<br>in small increments.</p></div>
    <div class="step" style="left:351px"><div class="time">20 minutes</div><div class="num">2</div><h3>LESSON PRACTICE</h3><p>Opportunity for students to<br>practice skills of new math<br>concepts.</p></div>
    <div class="step" style="left:698px"><div class="time">45 minutes</div><div class="num">3</div><h3>HOMEWORK</h3><p>Twenty-five to thirty problems to provide students with distributed practice that promote long-term retention of math concepts.</p></div>
  </div>
  <p class="total">1 hour and 30 minutes per session</p>
  <a class="btn btn-navy">Free Consultation</a>
</section>

<footer class="site-footer">
  <div class="footer-brand">
    <div class="brand-mark"></div>
    <div>
      <div class="brand-name">Trivento Numérica</div>
      <div class="brand-tag">Inspiring Math · Empowering Learning</div>
    </div>
  </div>
  <nav class="footer-nav"><span>Home</span><span>Features</span><span>Program</span><span>Tuition</span><span>About Us</span><span>Contact Us</span></nav>
  <p class="copyright">Copyrights@2025.Company Name.All Rights Reserved</p>
</footer>

</body>
</html>
```